Business Card Design

I need a business card for company that is a limited company that was originally an off-road vehicle company (atv's side by sides snowmobiles and motorcycles) and I have recently sold the assets of the company that was operating under a different name and have become semi retired. I continue to do maintenance on these types of vehicles and also sell and install parts and accessories. Recently I have also contracted to a snowmobile club to operate their groomer to groom the snowmobile trails. I would like bright and bold colors.
Industry/Entity Type
Club
Contact Information for Business Card
KTV Holdings Ltd.
Milo Fenwick
780-413-2769

```html
<!DOCTYPE html>
<html lang="en">
<head>
<meta charset="utf-8">
<title>KTV Holdings Ltd. – Business Card</title>
<link rel="stylesheet" href="https://fonts.googleapis.com/css2?family=Arvo:wght@400;700&display=swap">
<style>
  :root {
    --stage: #0b3a8c;
    --card-yellow: #fff200;
    --card-black: #050505;
    --ink-black: #000000;
    --ink-yellow: #fff200;
  }
  * { box-sizing: border-box; margin: 0; padding: 0; }
  html, body { width: 1200px; height: 1000px; overflow: hidden; }
  body {
    background: var(--stage);
    position: relative;
    font-family: "Arvo", serif;
  }
  .card {
    position: absolute;
    top: 190px;
    width: 362px;
    height: 618px;
    border-radius: 14px;
    overflow: hidden;
  }
  .card--front { left: 227px; background: var(--card-yellow); }
  .card--back  { left: 611px; background: var(--card-black); color: var(--ink-yellow); }

  .sled-art {
    position: absolute;
    border-radius: 40px 60px 20px 30px;
  }
  .card--front .sled-art {
    left: 0; top: 130px; width: 303px; height: 210px;
    background: var(--ink-black);
    border-radius: 0 70px 40px 0;
  }
  .card--back .sled-art {
    left: 124px; top: 430px; width: 238px; height: 162px;
    background: var(--ink-yellow);
    border-radius: 70px 0 0 40px;
  }

  .brand-name {
    position: absolute;
    left: 0; right: 0; top: 370px;
    text-align: center;
    color: var(--ink-black);
    font-weight: 700;
    line-height: 1;
  }
  .brand-name__main { display: block; font-size: 96px; letter-spacing: 4px; }
  .brand-name__sub { display: block; font-size: 30px; margin-top: 14px; letter-spacing: 1px; }

  .person-name {
    position: absolute; left: 0; right: 0; top: 152px;
    text-align: center; font-size: 28px; font-weight: 400;
  }
  .credentials {
    position: absolute; left: 0; right: 0; top: 236px;
    list-style: none; text-align: center;
    font-size: 14.5px; line-height: 22px;
  }
  .contact {
    position: absolute; left: 0; right: 0; top: 360px;
    text-align: center; font-size: 21px; line-height: 28px;
  }
  .contact__email { display: block; padding-left: 50px; }
</style>
</head>
<body>
  <section class="card card--front">
    <div class="sled-art" role="img" aria-label="Black silhouette of a snowmobile jumping"></div>
    <h1 class="brand-name">
      <span class="brand-name__main">KTV</span>
      <span class="brand-name__sub">HOLDINGS LTD.</span>
    </h1>
  </section>

  <section class="card card--back">
    <h2 class="person-name">Milo Fenwick</h2>
    <ul class="credentials">
      <li>Journeyman Red Seal Automotive Technician</li>
      <li>Journeyman Red Seal Motorcycle Technician</li>
      <li>Journeyman Parts Man</li>
    </ul>
    <p class="contact">
      <span class="contact__phone">780.413.2769</span><br>
      <span class="contact__email">ktvhold.77@mailbox.ca</span>
    </p>
    <div class="sled-art" role="img" aria-label="Yellow silhouette of a snowmobile riding"></div>
  </section>
</body>
</html>
```